Tavio's Pizzeria Direct Mail Postcard

Looking for a direct mail postcard with a similar design as the one attached, with our logo and store information. This has to meet rlmt direct mail standards and have the postage block printed on the back of cards. I will send over text edits once we get the design we like. The back of the card can have store info and coupons, just have to make sure the coupons on the back dont match the same space as coupons on the front so customers can cut them out. Please use the attached card as a guide. I want to have the same basic design

Industry/Entity Type

Pizza Delivery

Colors

Designer to choose colors to be used in the design.

Requirements
Must have
• RLMT Direct Mail capability
Nice to have
• Great pictures

```html
<!DOCTYPE html>
<html lang="en">
<head>
<meta charset="utf-8">
<title>Tavio's Pizzeria Direct Mail Postcard</title>
<link rel="stylesheet" href="https://fonts.googleapis.com/css2?family=Oswald:wght@500;700&family=Open+Sans:wght@400;600;700&display=swap">
<style>
  :root {
    --page: #ece7df;
    --brick-dark: #3e1c0e;
    --brick-mid: #6a3219;
    --wood-dark: #2e1a0f;
    --wood-mid: #5a3820;
    --coupon: #c9a77a;
    --coupon-light: #dcc29a;
    --coupon-edge: #a8855a;
    --price-red: #d4161b;
    --price-yellow: #f4c21a;
    --sub-red: #b3201a;
    --sub-brown: #5a2e14;
    --fine: #5b4330;
    --frame-dark: #1d1d1d;
    --frame-light: #f2f2f2;
    --white: #ffffff;
    --logo-red: #d3161e;
    --photo-crust: #d9a15c;
    --photo-sauce: #a8442a;
    --photo-cheese: #efd9a6;
  }
  * { box-sizing: border-box; margin: 0; padding: 0; }
  html, body { width: 1000px; height: 1200px; overflow: hidden; }
  body { background: var(--page); font-family: "Open Sans", Arial, sans-serif; position: relative; }

  .postcard { position: absolute; left: 118px; width: 764px; overflow: hidden; }
  .postcard--front { top: 83px; height: 491px;
    background: linear-gradient(135deg, var(--brick-mid), var(--brick-dark) 55%, var(--brick-mid)); }
  .postcard--back { top: 636px; height: 493px;
    background: linear-gradient(100deg, var(--wood-dark), var(--wood-mid) 45%, var(--wood-dark)); }

  .brand { position: absolute; left: 37px; top: 22px; width: 112px; display: flex; flex-direction: column; align-items: center; gap: 6px; }
  .brand__mark { width: 44px; height: 44px; border-radius: 50%; background: var(--logo-red); }
  .brand__name { font-weight: 700; font-size: 15px; line-height: 1.15; color: var(--white); text-align: center; }

  .coupon { position: absolute; border-radius: 12px; text-align: center;
    background: radial-gradient(ellipse at 50% 30%, var(--coupon-light), var(--coupon) 70%);
    border: 1px solid var(--coupon-edge); box-shadow: 0 2px 6px rgba(0,0,0,.35); }
  .coupon__price { font-family: "Oswald", Arial Narrow, sans-serif; font-weight: 700; line-height: 1; }
  .coupon__amount { color: var(--price-red); }
  .coupon__amount sup { font-size: .55em; vertical-align: .7em; }
  .coupon__off { color: var(--price-yellow); }
  .coupon__item { font-family: "Oswald", Arial Narrow, sans-serif; font-weight: 500; color: var(--sub-brown); line-height: 1.1; }
  .coupon__range { color: var(--sub-red); }
  .coupon__fine { color: var(--fine); line-height: 1.35; margin: 0 auto; }

  .coupon--large { left: 39px; width: 234px; height: 144px; padding-top: 22px; }
  .coupon--large .coupon__price { font-size: 40px; }
  .coupon--large .coupon__item { font-size: 24px; margin-top: 2px; }
  .coupon--large .coupon__fine { font-size: 6px; width: 190px; margin-top: 10px; }

  .coupon--small { width: 156px; height: 96px; padding-top: 14px; }
  .coupon--small .coupon__price { font-size: 24px; }
  .coupon--small .coupon__item { font-size: 13px; margin-top: 1px; }
  .coupon--small .coupon__fine { font-size: 6px; width: 138px; margin-top: 4px; }

  .photo-frame { position: absolute; background: var(--frame-dark); padding: 7px; box-shadow: 0 3px 8px rgba(0,0,0,.5); }
  .photo-frame__inner { width: 100%; height: 100%; border: 3px solid var(--frame-light);
    background: radial-gradient(circle at 50% 55%, var(--photo-sauce), var(--photo-crust) 55%, var(--photo-cheese)); }
  .photo-frame--hero { padding: 10px; }

  .contact--front { position: absolute; left: 425px; top: 404px; color: var(--white); }
  .contact__call { font-size: 29px; font-weight: 600; line-height: 1.1; }
  .contact__web { display: flex; align-items: center; gap: 7px; font-size: 15px; font-weight: 700; margin-top: 10px; margin-left: 86px; }
  .contact__web svg { width: 12px; height: 12px; }

  .contact--back { position: absolute; left: 42px; top: 402px; color: var(--white); }
  .contact--back .contact__label { font-size: 19px; line-height: 1.2; }
  .contact--back .contact__phone { font-size: 19px; font-weight: 700; line-height: 1.2; }
  .contact--back .contact__web { margin: 8px 0 0; font-size: 14px; }

  .pizza-box-photo { position: absolute; left: 358px; top: 0; width: 406px; height: 493px;
    clip-path: polygon(0 20%, 28% 0, 100% 0, 100% 100%, 25% 100%);
    background: radial-gradient(circle at 70% 45%, var(--photo-cheese), var(--photo-crust) 60%, #e8e2d8 75%); }
  .mail-block { position: absolute; background: var(--white); }
  .mail-block--postage { left: 645px; top: 11px; width: 112px; height: 82px; }
  .mail-block--address { left: 507px; top: 214px; width: 257px; height: 279px; }
  .mail-block--address-foot { left: 330px; top: 427px; width: 178px; height: 66px; }
</style>
</head>
<body>

<section class="postcard postcard--front" aria-label="Postcard front">
  <div class="brand"><span class="brand__mark"></span><span class="brand__name">Tavio's Pizzeria</span></div>

  <div class="coupon coupon--large" style="top:149px">
    <div class="coupon__price"><span class="coupon__amount"><sup>$</sup>100</span> <span class="coupon__off">OFF</span></div>
    <div class="coupon__item"><span class="coupon__range">Any 5 - 10</span> Pizza</div>
    <p class="coupon__fine">It is a long established fact that a reader will be distracted by the readable content of a page when looking at its layout.</p>
  </div>
  <div class="coupon coupon--large" style="top:318px">
    <div class="coupon__price"><span class="coupon__amount"><sup>$</sup>200</span> <span class="coupon__off">OFF</span></div>
    <div class="coupon__item"><span class="coupon__range">Any 12 - 14</span> Pizza</div>
    <p class="coupon__fine">It is a long established fact that a reader will be distracted by the readable content of a page when looking at its layout.</p>
  </div>

  <div class="photo-frame" style="left:263px;top:25px;width:146px;height:107px"><div class="photo-frame__inner" role="img" aria-label="Photo of a spinach and tomato pizza"></div></div>
  <div class="photo-frame" style="left:425px;top:25px;width:146px;height:107px"><div class="photo-frame__inner" role="img" aria-label="Photo of a rocket pizza on a wooden board"></div></div>
  <div class="photo-frame" style="left:590px;top:25px;width:144px;height:107px"><div class="photo-frame__inner" role="img" aria-label="Photo of a cherry tomato pizza"></div></div>
  <div class="photo-frame photo-frame--hero" style="left:415px;top:145px;width:325px;height:237px"><div class="photo-frame__inner" role="img" aria-label="Close-up photo of a meat and olive pizza"></div></div>

  <div class="contact contact--front">
    <div class="contact__call">Call Us:1234 555 018</div>
    <div class="contact__web">
      <svg viewBox="0 0 12 12" aria-hidden="true"><circle cx="6" cy="6" r="5.3" fill="none" stroke="#fff" stroke-width="1.2"/><path d="M0.7 6h10.6M6 0.7c-2.6 3-2.6 7.6 0 10.6M6 0.7c2.6 3 2.6 7.6 0 10.6" fill="none" stroke="#fff" stroke-width="1"/></svg>
      <span>www.taviospizzeria.com</span>
    </div>
  </div>
</section>

<section class="postcard postcard--back" aria-label="Postcard back">
  <div class="pizza-box-photo" role="img" aria-label="Photo of a ham and mushroom pizza in an open box"></div>
  <div class="mail-block mail-block--postage" aria-label="Postage area"></div>
  <div class="mail-block mail-block--address" aria-label="Address area"></div>
  <div class="mail-block mail-block--address-foot"></div>

  <div class="brand"><span class="brand__mark"></span><span class="brand__name">Tavio's Pizzeria</span></div>

  <div class="coupon coupon--small" style="left:39px;top:162px">
    <div class="coupon__price"><span class="coupon__amount"><sup>$</sup>50</span> <span class="coupon__off">OFF</span></div>
    <div class="coupon__item">Extra Large Pizza</div>
    <p class="coupon__fine">It is a long established fact that a reader will be distracted by the readable content of a page when looking at its layout.</p>
  </div>
  <div class="coupon coupon--small" style="left:215px;top:162px">
    <div class="coupon__price"><span class="coupon__amount"><sup>$</sup>30</span> <span class="coupon__off">OFF</span></div>
    <div class="coupon__item">Large Pizza</div>
    <p class="coupon__fine">It is a long established fact that a reader will be distracted by the readable content of a page when looking at its layout.</p>
  </div>
  <div class="coupon coupon--small" style="left:39px;top:276px">
    <div class="coupon__price"><span class="coupon__amount"><sup>$</sup>20</span> <span class="coupon__off">OFF</span></div>
    <div class="coupon__item">Medium Pizza</div>
    <p class="coupon__fine">It is a long established fact that a reader will be distracted by the readable content of a page when looking at its layout.</p>
  </div>
  <div class="coupon coupon--small" style="left:215px;top:276px">
    <div class="coupon__price"><span class="coupon__amount"><sup>$</sup>10</span> <span class="coupon__off">OFF</span></div>
    <div class="coupon__item">Small Pizza</div>
    <p class="coupon__fine">It is a long established fact that a reader will be distracted by the readable content of a page when looking at its layout.</p>
  </div>

  <div class="contact contact--back">
    <div class="contact__label">Call Us</div>
    <div class="contact__phone">1234 555 018</div>
    <div class="contact__web">
      <svg viewBox="0 0 12 12" aria-hidden="true"><circle cx="6" cy="6" r="5.3" fill="none" stroke="#fff" stroke-width="1.2"/><path d="M0.7 6h10.6M6 0.7c-2.6 3-2.6 7.6 0 10.6M6 0.7c2.6 3 2.6 7.6 0 10.6" fill="none" stroke="#fff" stroke-width="1"/></svg>
      <span>www.taviospizzeria.com</span>
    </div>
  </div>
</section>

</body>
</html>
```